Lantern Business Cards

Need business cards for my employees at my restaurant.

Needs to include:
Our Logo
Lantern Bowls & Brews
Name: Nora Pettigrew
Title : Owner
Address: 487 Mirella Ave. Lake Havasu City, AZ 86519
Web: www.lanternkestrel.com
Phone: 928-555-0147
Cell: 928-555-0192
Email: info@lanternkestrel.com

```html
<!DOCTYPE html>
<html lang="en">
<head>
<meta charset="utf-8">
<title>Lantern Business Cards</title>
<link rel="stylesheet" href="https://fonts.googleapis.com/css2?family=Roboto:wght@400;700&display=swap">
<style>
  :root {
    --stage: #1d1d1d;
    --card: #ffffff;
    --brand-red: #c41f2f;
    --accent-red: #e4303a;
    --ink: #1a1a1a;
    --rule: #3a3a3a;
  }
  * { margin: 0; padding: 0; box-sizing: border-box; }
  html, body { width: 1200px; height: 1059px; overflow: hidden; }
  body {
    background: var(--stage);
    font-family: "Roboto", Arial, sans-serif;
    color: var(--ink);
    position: relative;
  }
  .card {
    position: absolute;
    background: var(--card);
    border-radius: 24px;
  }
  .card--front { left: 256px; top: 94px; width: 702px; height: 402px; }
  .card--back  { left: 230px; top: 533px; width: 720px; height: 411px; }

  .brand {
    position: absolute;
    display: flex;
    flex-direction: column;
    align-items: center;
    text-align: center;
    color: var(--brand-red);
    font-weight: 700;
  }
  .brand__dot {
    border-radius: 50%;
    background: var(--brand-red);
  }
  .brand__name { line-height: 1.05; }

  .card--front .brand { left: 66px; top: 116px; width: 270px; }
  .card--front .brand__dot { width: 52px; height: 52px; margin-bottom: 14px; }
  .card--front .brand__name { font-size: 30px; }

  .card--back .brand { left: 160px; top: 82px; width: 400px; }
  .card--back .brand__dot { width: 90px; height: 90px; margin-bottom: 22px; }
  .card--back .brand__name { font-size: 48px; }

  .divider {
    position: absolute;
    left: 357px; top: 88px;
    width: 2px; height: 227px;
    background: var(--rule);
  }
  .contact { position: absolute; left: 390px; top: 74px; }
  .contact__name {
    color: var(--accent-red);
    font-weight: 700;
    font-size: 25px;
    line-height: 32px;
  }
  .contact__title { font-size: 18px; line-height: 24px; margin-top: 2px; }
  .contact__address { font-size: 18.5px; line-height: 23px; margin-top: 16px; }
  .contact__list { list-style: none; margin-top: 12px; }
  .contact__item {
    display: flex; align-items: center;
    font-size: 19px; height: 31px;
  }
  .contact__icon { width: 18px; height: 18px; margin-right: 8px; flex: none; fill: var(--accent-red); }
</style>
</head>
<body>
  <section class="card card--front">
    <div class="brand">
      <span class="brand__dot"></span>
      <span class="brand__name">Lantern<br>Bowls &amp; Brews</span>
    </div>
    <div class="divider"></div>
    <div class="contact">
      <p class="contact__name">Nora Pettigrew</p>
      <p class="contact__title">Owner</p>
      <p class="contact__address">487 Mirella Ave. Lake<br>Havasu City, AZ 86519</p>
      <ul class="contact__list">
        <li class="contact__item">
          <svg class="contact__icon" viewBox="0 0 24 24"><path d="M6.6 10.8a15.1 15.1 0 0 0 6.6 6.6l2.2-2.2c.3-.3.7-.4 1-.2 1.1.4 2.3.6 3.6.6.6 0 1 .4 1 1V20c0 .6-.4 1-1 1A17 17 0 0 1 3 4c0-.6.4-1 1-1h3.5c.6 0 1 .4 1 1 0 1.3.2 2.5.6 3.6.1.3 0 .7-.2 1z"/></svg>
          928-555-0147
        </li>
        <li class="contact__item">
          <svg class="contact__icon" viewBox="0 0 24 24"><path d="M7 1h10a2 2 0 0 1 2 2v18a2 2 0 0 1-2 2H7a2 2 0 0 1-2-2V3a2 2 0 0 1 2-2zm0 3v14h10V4zm5 15.5a1 1 0 1 0 0 2 1 1 0 0 0 0-2z"/></svg>
          928-555-0192
        </li>
        <li class="contact__item">
          <svg class="contact__icon" viewBox="0 0 24 24"><path d="M2 5h20v14H2zm2 2v.5l8 5.5 8-5.5V7z"/></svg>
          info@lanternkestrel.com
        </li>
        <li class="contact__item">
          <svg class="contact__icon" viewBox="0 0 24 24"><path d="M12 2a10 10 0 1 0 0 20 10 10 0 0 0 0-20zm-1 17.9A8 8 0 0 1 4.1 10l4.9 5v1a2 2 0 0 0 2 2zm6.9-2.5A2 2 0 0 0 16 16h-1v-3a1 1 0 0 0-1-1H8v-2h2a1 1 0 0 0 1-1V7h2a2 2 0 0 0 2-2v-.4a8 8 0 0 1 2.9 12.8z"/></svg>
          www.lanternkestrel.com
        </li>
      </ul>
    </div>
  </section>

  <section class="card card--back">
    <div class="brand">
      <span class="brand__dot"></span>
      <span class="brand__name">Lantern<br>Bowls &amp; Brews</span>
    </div>
  </section>
</body>
</html>
```